Simple Floral Service Web-Banner

I need to put a banner add on the members section of a website for an organization in which we are members.

The ad size is 470px x 214px.

I am uploading 4 pictures. 1 is a picture of red roses, and 1 is a picture of a t-shirt. These are 2 major products of ours which need to be incorporated in the banner. I do not have these in higher res or vectorized format, so please work with what you have. I am also uploading our 2 logos, one is for our Canadian company, and one for our American company. Both logos should be included at equal sizes.

The following text should be used:
"Proudly providing top quality roses, and custom commemorative grad t-shirts at over 800 schools."

I am just looking for a simple banner incorporating those pictures and that wording. I don't want something that is overly flashy.

I will monitor the submissions in a timely manner and give you feedback.

```html
<!DOCTYPE html>
<html lang="en">
<head>
<meta charset="utf-8">
<title>Roses and Grad T-Shirts Banner</title>
<link rel="stylesheet" href="https://fonts.googleapis.com/css2?family=Oswald:wght@500;600;700&display=swap">
<style>
  :root {
    --green-light: #74ad45;
    --green-mid: #5c9636;
    --green-deep: #447a26;
    --green-ink: #235d1c;
    --white: #ffffff;
    --band-top: #ffffff;
    --band-bottom: #e4e8df;
    --rose-red: #b8141c;
    --rose-leaf: #4f7a3a;
    --shirt-grey: #e9ebe7;
    --shirt-shadow: #c9cdc4;
  }
  * { margin: 0; padding: 0; box-sizing: border-box; }
  html, body { width: 1200px; height: 546px; overflow: hidden; }
  body { font-family: "Oswald", "Arial Narrow", sans-serif; }

  .banner {
    position: relative;
    width: 1200px;
    height: 546px;
    overflow: hidden;
    background: radial-gradient(ellipse at 45% 35%, var(--green-light) 0%, var(--green-mid) 55%, var(--green-deep) 100%);
  }

  .product { position: absolute; z-index: 1; }
  .product--roses {
    left: 150px; top: 170px; width: 350px; height: 240px;
    background: radial-gradient(ellipse at 50% 55%, var(--rose-red) 0%, #8e1016 45%, var(--rose-leaf) 78%, rgba(79,122,58,0) 100%);
    border-radius: 45%;
  }
  .product--shirts {
    left: 608px; top: 236px; width: 380px; height: 172px;
    background: linear-gradient(135deg, var(--white) 0%, var(--shirt-grey) 55%, var(--shirt-shadow) 100%);
    border-radius: 22px;
  }

  .headline {
    position: absolute;
    z-index: 2;
    margin: 0;
    font-size: inherit;
    color: var(--white);
    text-transform: uppercase;
    font-weight: 600;
    text-shadow: 0 2px 3px rgba(0, 0, 0, 0.3);
  }
  .headline .line {
    position: absolute;
    display: block;
    line-height: 1;
    white-space: nowrap;
  }
  .headline .small { font-size: 53px; letter-spacing: 0.3px; }
  .headline .big { font-size: 94px; font-weight: 700; letter-spacing: -0.5px; }

  .headline--roses { left: 0; top: 0; width: 600px; height: 220px; }
  .headline--roses .l1 { left: 31px; top: 14px; }
  .headline--roses .l2 { left: 31px; top: 78px; }
  .headline--roses .l3 { left: 318px; top: 98px; }

  .headline--shirts { left: 600px; top: 0; width: 600px; height: 240px; }
  .headline--shirts .l1 { left: 59px; top: 14px; }
  .headline--shirts .l2 { left: 59px; top: 80px; }
  .headline--shirts .l3 { right: 38px; top: 143px; font-size: 80px; }

  .footer-band {
    position: absolute;
    left: 0; right: 0; bottom: 0;
    height: 130px;
    z-index: 3;
    background: linear-gradient(180deg, var(--band-top), var(--band-bottom));
    border-top: 3px solid var(--green-ink);
    display: flex;
    align-items: center;
    justify-content: space-between;
    padding: 0 38px 0 25px;
  }
  .brand {
    display: flex;
    align-items: center;
    gap: 10px;
    color: var(--green-ink);
    font-weight: 600;
    font-size: 32px;
    line-height: 1.1;
    width: 250px;
  }
  .brand--right { justify-content: flex-end; text-align: right; }
  .brand .dot {
    width: 14px; height: 14px; border-radius: 50%;
    background: var(--green-ink);
    flex: none;
  }
  .reach {
    color: var(--green-ink);
    font-weight: 600;
    font-size: 44px;
    text-transform: uppercase;
    letter-spacing: 0.5px;
    line-height: 1;
    white-space: nowrap;
    padding-top: 30px;
  }
</style>
</head>
<body>
  <div class="banner">
    <div class="product product--roses" role="img" aria-label="Photo of a wrapped bouquet of red roses with baby's breath"></div>
    <div class="product product--shirts" role="img" aria-label="Photo of two white commemorative graduation t-shirts, front and back"></div>

    <h1 class="headline headline--roses">
      <span class="line small l1">Proudly Providing</span>
      <span class="line small l2">Top Quality</span>
      <span class="line big l3">Roses</span>
    </h1>

    <h2 class="headline headline--shirts">
      <span class="line small l1">Custom</span>
      <span class="line small l2">Commemorative Grad</span>
      <span class="line big l3">T-Shirts</span>
    </h2>

    <div class="footer-band">
      <div class="brand brand--left">
        <span class="dot"></span>
        <span class="name">Laurel Day<br>Flowers</span>
      </div>
      <div class="reach">At Over 800 Schools</div>
      <div class="brand brand--right">
        <span class="name">Capstone<br>Flowers</span>
        <span class="dot"></span>
      </div>
    </div>
  </div>
</body>
</html>
```